We are looking to have a very professional, simple, and timeless design for a brochure that we will be handing out personally to possible clients. We are looking for something NEW , FRESH, and INNOVATIVE, but NOT TRENDY. We have already purchased a business card design from pixel harbor. The only thing that must stay the same is the type of font "K.T. Bookkeeping Services" is in. The files below are ideas we have used or liked and are wanting something of that nature for the brochure. If you have any questions please feel free to email me.

```html
<!DOCTYPE html>
<html lang="en">
<head>
<meta charset="utf-8">
<title>K.T. Bookkeeping Services — Brochure</title>
<link rel="stylesheet" href="https://fonts.googleapis.com/css2?family=Crimson+Text:ital,wght@0,400;0,700;1,700&display=swap">
<style>
  :root {
    --navy: #1b5f86;
    --wine: #5a1c1f;
    --wine-deep: #4a1719;
    --mist: #f1f1f1;
    --slate: #b9b9b9;
    --heading: #6b1f22;
    --ink: #2f2a2a;
    --panel-fill: rgba(255, 255, 255, 0.42);
    --panel-edge: #7a7a7a;
    --paper: #ffffff;
  }
  * { box-sizing: border-box; margin: 0; padding: 0; }
  html, body {
    width: 1200px;
    height: 729px;
    overflow: hidden;
    background: var(--paper);
  }
  .brochure {
    position: relative;
    width: 1200px;
    height: 729px;
    overflow: hidden;
    font-family: "Crimson Text", Georgia, serif;
    color: var(--ink);
  }
  .backdrop {
    position: absolute;
    inset: 0;
    background: linear-gradient(128deg,
      var(--navy) 0%,
      var(--navy) 20%,
      var(--mist) 44%,
      var(--slate) 56%,
      var(--wine) 70%,
      var(--wine-deep) 100%);
  }
  .panel {
    position: absolute;
    top: 44px;
    height: 641px;
    background: var(--panel-fill);
    border: 1px solid var(--panel-edge);
    padding: 0 22px;
  }
  .panel--left   { left: 43px;  width: 360px; }
  .panel--middle { left: 421px; width: 358px; }
  .panel--right  { left: 797px; width: 359px; }

  .brand-name {
    color: var(--paper);
    font-family: "Crimson Text", Georgia, serif;
    font-weight: 400;
    font-size: 26px;
    line-height: 28px;
    width: 170px;
  }
  .panel--left .brand-name {
    margin-top: 21px;
  }
  .panel--right .brand-name {
    position: absolute;
    left: 178px;
    top: 511px;
  }

  .panel-title {
    font-weight: 400;
    font-size: 36px;
    line-height: 40px;
    color: var(--heading);
  }
  .panel--left .panel-title { margin-top: 26px; }
  .panel--middle .panel-title,
  .panel--right .panel-title { margin-top: 22px; }

  .lead {
    font-style: italic;
    font-weight: 700;
    font-size: 14px;
    line-height: 17.5px;
    text-indent: 14px;
    margin-top: 12px;
  }

  .body-text {
    font-size: 14.5px;
    line-height: 17.5px;
    text-align: justify;
    hyphens: auto;
  }
  .body-text + .body-text { margin-top: 16px; }
  .lead + .body-text { margin-top: 32px; }
  .body-text--spaced { margin-top: 34px !important; }
  .body-text--tight { margin-top: 0 !important; }
</style>
</head>
<body>
<main class="brochure">
  <div class="backdrop" role="img" aria-label="Background sweeping from navy blue at the top left through soft grey to deep wine red at the bottom right"></div>

  <section class="panel panel--left">
    <p class="brand-name">K.T. Bookkeeping Services</p>
    <h2 class="panel-title">Lorem ipsum</h2>
    <p class="lead">Lorem ipsum dolor sit amet, consectetur adipiscing elit. Aenean in tortor sit amet odio aliquam facilisis. Sed ac sodales tortor. Integer ornare nec erat ac rhoncus.</p>
    <p class="body-text">Donec sit amet elit quis ligula vulputate maximus a ac quam. Etiam bibendum pellentesque enim, iaculis iaculis libero. Donec semper dictum quam, at auctor quam consectetur non.</p>
    <p class="body-text body-text--spaced">Phasellus felis felis, euismod non placerat ac, congue vel neque. Ut ut est malesuada massa dignissim bibendum sed id nulla. Donec tristique velit at sagittis ultricies. Proin et iaculis felis.</p>
    <p class="body-text">Aliquam rutrum gravida accumsan. Pellentesque vitae metus sit amet sem tempor sodales et id nisi. Phasellus sed sem ornare, tincidunt lectus ornare, condimentum libero.</p>
  </section>

  <section class="panel panel--middle">
    <h2 class="panel-title">Lorem ipsum</h2>
    <p class="lead">Sed ac sodales tortor. Integer ornare nec erat ac rhoncus. Donec sit amet elit quis ligula vulputate maximus a ac quam. Etiam bibendum pellentesque enim, iaculis iaculis libero.</p>
    <p class="body-text">Donec semper dictum quam, at auctor quam consectetur non. Phasellus felis felis, euismod non placerat ac, congue vel neque.</p>
    <p class="body-text">Ut ut est malesuada massa dignissim bibendum sed id nulla. Donec tristique velit at sagittis ultricies. Proin et iaculis felis.</p>
    <p class="body-text">Aliquam rutrum gravida accumsan. Pellentesque vitae metus sit amet sem tempor sodales et id nisi. Phasellus sed sem ornare, tincidunt lectus ornare, condimentum libero.</p>
    <p class="body-text body-text--spaced">Praesent ut semper ipsum. Morbi non velit vel lacus tincidunt dictum.</p>
    <p class="body-text">Aliquam rutrum gravida accumsan. Pellentesque vitae metus sit amet sem tempor sodales et id nisi. Phasellus sed sem ornare, tincidunt lectus ornare, condimentum libero.</p>
    <p class="body-text body-text--tight">Praesent ut semper ipsum. Morbi non velit vel lacus tincidunt dictum.</p>
  </section>

  <section class="panel panel--right">
    <h2 class="panel-title">Lorem ipsum</h2>
    <p class="lead">Sed ac sodales tortor. Integer ornare nec erat ac rhoncus. Donec sit amet elit quis ligula vulputate maximus a ac quam. Etiam bibendum pellentesque enim, iaculis iaculis libero.</p>
    <p class="body-text">Donec semper dictum quam, at auctor quam consectetur non. Phasellus felis felis, euismod non placerat ac, congue vel neque.</p>
    <p class="body-text">Ut ut est malesuada massa dignissim bibendum sed id nulla. Donec tristique velit at sagittis ultricies. Proin et iaculis felis.</p>
    <p class="body-text">Aliquam rutrum gravida accumsan. Pellentesque vitae metus sit amet sem tempor sodales et id nisi. Phasellus sed sem ornare, tincidunt lectus ornare, condimentum libero.</p>
    <p class="body-text body-text--spaced">Praesent ut semper ipsum. Morbi non velit vel lacus tincidunt dictum.</p>
    <p class="brand-name">K.T. Bookkeeping Services</p>
  </section>
</main>
</body>
</html>
```